Luxury Business Card Design for High-End Window Treatments

Gilded Vantages
Custom Plantation Shutters & Architectural Shading Systems

⸻

BACK

Daniel Forsythe
Owner

Custom Interior & Exterior Window Treatments

919-482-7034
gildedvantages.com

I have included a picture that I’m hoping we can use on the back, but I’m also wondering if you can get rid of the ladder? Should we get rid of shutters , shades and blinds underneath Gilded Vantages?

Target Market(s)

High-end residential homeowners, custom home builders, architects, interior designers, and luxury renovation clients seeking premium plantation shutters and motorized architectural shading systems.

Industry/Entity Type

Custom Window treatments

Contact Information for Business Card

Front Gilded Vantages Custom Plantation Shutters Motorized Architectural Shading Systems BACK Daniel Forsythe Owner 919-482-7034 GildedVantages.com Custom Interior & Exterior Window Treatments By Appointment

Requirements
Nice to have
• Not 100% sure on nice to halves or the color but you can definitely check out my website to get a better understanding of what I’m trying to do

```html
<!DOCTYPE html>
<html lang="en">
<head>
<meta charset="utf-8">
<title>Gilded Vantages — Business Card</title>
<link href="https://fonts.googleapis.com/css2?family=Libre+Baskerville:wght@400;700&family=Montserrat:wght@400;500&display=swap" rel="stylesheet">
<style>
  :root {
    --backdrop: #2a2a2b;
    --card-gold: #a69464;
    --card-black: #060606;
    --cream: #efe9dc;
    --gold-bright: #f2c94c;
    --gold-soft: #cfae57;
    --white: #ffffff;
  }
  * { box-sizing: border-box; margin: 0; padding: 0; }
  html, body { width: 1200px; height: 875px; overflow: hidden; }
  body {
    background: var(--backdrop);
    display: flex;
    flex-direction: column;
    align-items: center;
    justify-content: center;
    gap: 56px;
    font-family: "Montserrat", sans-serif;
  }
  .card {
    width: 600px;
    height: 343px;
    border-radius: 22px;
    position: relative;
    overflow: hidden;
  }
  .card--front { background: var(--card-gold); }
  .card--back { background: var(--card-black); }

  .brand {
    position: absolute;
    left: 0; right: 0;
    text-align: center;
  }
  .brand__name {
    font-family: "Libre Baskerville", serif;
    font-weight: 400;
    color: var(--cream);
    letter-spacing: 0.5px;
    line-height: 1;
  }
  .brand__lines {
    font-family: "Libre Baskerville", serif;
    font-weight: 700;
    color: var(--gold-bright);
    word-spacing: 14px;
    margin-top: 16px;
  }
  .card--front .brand { top: 118px; }
  .card--front .brand__name { font-size: 44px; }
  .card--front .brand__lines { font-size: 20px; }

  .card--back .brand { top: 46px; }
  .card--back .brand__name { font-size: 34px; }
  .card--back .brand__lines { font-size: 15px; margin-top: 12px; }

  .contact-row {
    position: absolute;
    top: 160px;
    left: 0; right: 0;
    display: flex;
    justify-content: center;
    align-items: center;
    gap: 18px;
  }
  .person { text-align: right; }
  .person__name {
    font-family: "Libre Baskerville", serif;
    font-weight: 700;
    font-size: 22px;
    color: var(--gold-soft);
  }
  .person__role {
    font-size: 13px;
    color: var(--white);
    margin-top: 2px;
  }
  .divider {
    width: 1.5px;
    height: 74px;
    background: var(--gold-soft);
  }
  .details { list-style: none; font-size: 12.5px; color: var(--white); }
  .details li { display: flex; align-items: center; gap: 8px; line-height: 24px; }
  .details svg { width: 13px; height: 13px; fill: var(--gold-soft); }
  .details .appointment { color: var(--gold-bright); padding-left: 21px; }

  .services {
    position: absolute;
    bottom: 40px;
    left: 0; right: 0;
    text-align: center;
    font-size: 13px;
    color: var(--white);
    letter-spacing: 0.3px;
  }
</style>
</head>
<body>
  <section class="card card--front">
    <div class="brand">
      <div class="brand__name">Gilded Vantages</div>
      <div class="brand__lines">Shutters Shades Blinds</div>
    </div>
  </section>

  <section class="card card--back">
    <div class="brand">
      <div class="brand__name">Gilded Vantages</div>
      <div class="brand__lines">Shutters Shades Blinds</div>
    </div>

    <div class="contact-row">
      <div class="person">
        <div class="person__name">Daniel Forsythe</div>
        <div class="person__role">Owner</div>
      </div>
      <div class="divider"></div>
      <ul class="details">
        <li>
          <svg viewBox="0 0 24 24" aria-hidden="true"><path d="M6.6 10.8a15.1 15.1 0 0 0 6.6 6.6l2.2-2.2a1 1 0 0 1 1-.25 11.4 11.4 0 0 0 3.6.57 1 1 0 0 1 1 1V20a1 1 0 0 1-1 1A17 17 0 0 1 3 4a1 1 0 0 1 1-1h3.5a1 1 0 0 1 1 1c0 1.25.2 2.45.57 3.57a1 1 0 0 1-.25 1z"/></svg>
          919-482-7034
        </li>
        <li>
          <svg viewBox="0 0 24 24" aria-hidden="true"><path d="M12 2a10 10 0 1 0 0 20 10 10 0 0 0 0-20zm6.9 6h-2.9a15.6 15.6 0 0 0-1.4-3.6A8 8 0 0 1 18.9 8zM12 4a14 14 0 0 1 1.9 4h-3.8A14 14 0 0 1 12 4zM4.3 14a8 8 0 0 1 0-4h3.4a16 16 0 0 0 0 4zm.8 2h2.9a15.6 15.6 0 0 0 1.4 3.6A8 8 0 0 1 5.1 16zM8 8H5.1a8 8 0 0 1 4.3-3.6A15.6 15.6 0 0 0 8 8zm4 12a14 14 0 0 1-1.9-4h3.8A14 14 0 0 1 12 20zm2.3-6H9.7a14.6 14.6 0 0 1 0-4h4.6a14.6 14.6 0 0 1 0 4zm.3 5.6a15.6 15.6 0 0 0 1.4-3.6h2.9a8 8 0 0 1-4.3 3.6zM16.3 14a16 16 0 0 0 0-4h3.4a8 8 0 0 1 0 4z"/></svg>
          GildedVantages.com
        </li>
        <li class="appointment">By Appointment</li>
      </ul>
    </div>

    <p class="services">Custom Interior &amp; Exterior Window Treatments</p>
  </section>
</body>
</html>
```